Bref créative
Business card for an optometrist
Professional
Dr. Toren "Bax" Holmqvist
Optometric Physician
418 Marlow Lane, 2nd Floor, Fernbrook, NJ 07135
Visioncare.Fernbrook@quilmail.com
www.fernbrookvisioncare.com
NJ Lic. #4817
We would like to have Fernbrook Visioncare logo as the first line followed by the doctor's name and license number. Then either in the center or at the bottom right/left, we would like the address, phone & fax number and email/website.
M_____________________________
HAS AN APPOINTMENT ON
and then show boxes for each day of the wk (excluding sunday) and then:
DATE_______AT____________(AM/PM)
IF UNABLE TO KEEP APPOINTMENT, KINDLY GIVE 24 HOURS NOTICE

```html
<!DOCTYPE html>
<html lang="en">
<head>
<meta charset="utf-8">
<title>Fernbrook Visioncare – Stationery</title>
<link href="https://fonts.googleapis.com/css2?family=Open+Sans:wght@400;600&display=swap" rel="stylesheet">
<style>
:root{
  --blue:#1a7cc1;
  --blue-dark:#155f96;
  --orange:#e2671f;
  --ink:#3b4450;
  --muted:#7d8590;
  --paper:#ffffff;
  --ground:#eef0f2;
  --edge:#dde1e5;
  --faint:#e6eef5;
}
*{box-sizing:border-box;margin:0;padding:0}
html,body{width:1200px;height:936px;overflow:hidden}
body{background:var(--ground);font-family:"Open Sans",Arial,sans-serif;color:var(--ink);position:relative}
.sheet{position:absolute;background:var(--paper);border:1px solid var(--edge);overflow:hidden}
.band{position:absolute;inset:0;width:100%;height:100%}
.brand-name{font-family:"Open Sans",Arial,sans-serif;font-weight:600;color:var(--blue-dark);text-transform:uppercase;letter-spacing:.12em;line-height:1.15;display:flex;align-items:center;gap:.5em}
.brand-dot{display:inline-block;border-radius:50%;background:var(--orange);flex:none}

/* letterhead */
.letterhead{left:182px;top:56px;width:390px;height:559px}
.letterhead .brand-name{position:absolute;left:36px;top:40px;font-size:11px}
.letterhead .brand-dot{width:12px;height:12px}
.letterhead .contact{position:absolute;left:226px;top:34px;font-size:5px;line-height:1.55;color:var(--muted)}
.letterhead .faint-mark{position:absolute;left:70px;top:190px;width:170px;height:170px;border-radius:50%;background:var(--faint)}

/* folder */
.folder{left:633px;top:38px;width:432px;height:577px}
.folder .brand-name{position:absolute;left:40px;right:70px;top:300px;justify-content:center;font-size:24px;flex-direction:column;text-align:center;gap:14px}
.folder .brand-dot{width:44px;height:44px}

/* business card */
.card-front{left:46px;top:653px;width:177px;height:101px}
.card-front .brand-name{position:absolute;left:8px;top:34px;font-size:7px;width:78px}
.card-front .brand-dot{width:8px;height:8px}
.card-front .details{position:absolute;left:92px;top:10px;right:6px;color:#fff;font-size:4.6px;line-height:1.45}
.card-front .details .doc{font-weight:600;font-size:5.4px}
.card-back{left:46px;top:769px;width:177px;height:109px;padding:10px 12px;font-size:4.8px;color:var(--ink);line-height:1.3}
.card-back .line{margin-bottom:6px}
.card-back .days{display:flex;gap:6px;margin:4px 0 8px}
.card-back .day{display:flex;align-items:center;gap:2px}
.card-back .box{width:7px;height:7px;border:1px solid var(--muted)}
.card-back .note{font-size:4.2px;color:var(--muted);margin-top:6px}

/* envelopes */
.envelope-front{left:266px;top:666px;width:430px;height:212px}
.envelope-front .brand-name{position:absolute;left:16px;top:26px;font-size:12px}
.envelope-front .brand-dot{width:14px;height:14px}
.envelope-back{left:736px;top:663px;width:425px;height:215px}
.envelope-back .flap-url{position:absolute;left:0;right:0;top:18px;text-align:center;color:#fff;font-size:7px;letter-spacing:.25em;text-transform:uppercase}
</style>
</head>
<body>

<section class="sheet letterhead">
  <svg class="band" viewBox="0 0 390 559" preserveAspectRatio="none" aria-hidden="true">
    <path d="M390 0H366C356 200 352 390 336 559H390Z" fill="var(--blue)"/>
    <path d="M358 0C348 200 343 390 325 559" stroke="var(--orange)" stroke-width="4" fill="none"/>
  </svg>
  <div class="brand-name"><span class="brand-dot"></span>Fernbrook Visioncare</div>
  <address class="contact">
    418 Marlow Lane, 2nd Floor,<br>Fernbrook, NJ 07135<br>Ph: (201) 555-0148<br>Fax: (201) 555-0149<br>Visioncare.Fernbrook@quilmail.com<br>www.fernbrookvisioncare.com
  </address>
  <div class="faint-mark" role="img" aria-label="Faint brand circle watermark"></div>
</section>

<section class="sheet folder">
  <svg class="band" viewBox="0 0 432 577" preserveAspectRatio="none" aria-hidden="true">
    <path d="M432 0H410C402 200 394 400 378 577H432Z" fill="var(--blue)"/>
    <path d="M400 0C392 200 383 400 365 577" stroke="var(--orange)" stroke-width="5" fill="none"/>
  </svg>
  <div class="brand-name"><span class="brand-dot"></span>Fernbrook Visioncare</div>
</section>

<section class="sheet card-front">
  <svg class="band" viewBox="0 0 177 101" preserveAspectRatio="none" aria-hidden="true">
    <path d="M177 0H90V101H177Z" fill="var(--blue)"/>
    <path d="M87 0V101" stroke="var(--orange)" stroke-width="2"/>
  </svg>
  <div class="brand-name"><span class="brand-dot"></span>Fernbrook Visioncare</div>
  <div class="details">
    <div class="doc">Dr. Toren "Bax" Holmqvist</div>
    <div>Optometric Physician</div>
    <div>NJ Lic. #4817</div>
    <br>
    <div>418 Marlow Lane, 2nd Floor,<br>Fernbrook, NJ 07135</div>
    <div>Ph: (201) 555-0148</div>
    <div>Fax: (201) 555-0149</div>
    <div>Visioncare.Fernbrook@quilmail.com</div>
    <div>www.fernbrookvisioncare.com</div>
  </div>
</section>

<section class="sheet card-back">
  <div class="line">M______________________________</div>
  <div>HAS AN APPOINTMENT ON</div>
  <div class="days">
    <span class="day"><span class="box"></span>M</span>
    <span class="day"><span class="box"></span>T</span>
    <span class="day"><span class="box"></span>W</span>
    <span class="day"><span class="box"></span>T</span>
    <span class="day"><span class="box"></span>F</span>
    <span class="day"><span class="box"></span>S</span>
  </div>
  <div>DATE________AT____________(AM/PM)</div>
  <div class="note">IF UNABLE TO KEEP APPOINTMENT, KINDLY GIVE 24 HOURS NOTICE</div>
</section>

<section class="sheet envelope-front">
  <div class="brand-name"><span class="brand-dot"></span>Fernbrook Visioncare</div>
</section>

<section class="sheet envelope-back">
  <svg class="band" viewBox="0 0 425 215" preserveAspectRatio="none" aria-hidden="true">
    <path d="M0 0H425V40C340 70 250 88 212 150C175 88 85 70 0 40Z" fill="var(--blue)"/>
    <path d="M0 120L170 215M425 120L255 215" stroke="var(--edge)" stroke-width="1" fill="none"/>
  </svg>
  <div class="flap-url">www.fernbrookvisioncare.com</div>
</section>

</body>
</html>
```